Forest Consultant/Timber Buyer needs a clean business card

We are a forestry consulting and timber buying company. We meet with private landowners and assist them with timber management and timber harvesting. We would like a professional business card, please no clip art. logo is blue and white but would like to see a gray,silver, or some other color incorporated. Would like basic contact info. Would like to the layout to be creative and sleek but masculine.

Target Market(s)

private landowners

Industry/Entity Type

Business

Contact Information for Business Card

name,position, cell number, office number, email, website. This might be to cluttered. Basic contact info is what we are looking for.

Contact info can all be on one side with logo on the other.

Font styles to use
Serif
Sans Serif

Colors
0255a3
ffffff
aaaaaa

Requirements
Must have
• We just want it professional.
Nice to have
• Creative layout.
Should not have
• please no clip art of log trucks etc.

```html
<!DOCTYPE html>
<html lang="en">
<head>
<meta charset="utf-8">
<title>Ridgeline Land &amp; Timber – Business Card</title>
<link href="https://fonts.googleapis.com/css2?family=Lato:wght@400;700&display=swap" rel="stylesheet">
<style>
  :root {
    --brand-blue: #0255a3;
    --deep-blue: #02478a;
    --silver: #aaaaaa;
    --paper: #ffffff;
    --ink: #1c1c1c;
    --backdrop: #e9e9e9;
  }
  * { box-sizing: border-box; margin: 0; padding: 0; }
  html, body {
    width: 1200px; height: 900px; overflow: hidden;
    background: var(--backdrop);
    font-family: "Lato", sans-serif;
  }
  .stage { position: relative; width: 1200px; height: 900px; }
  .card {
    position: absolute; width: 700px; height: 400px;
    box-shadow: 0 10px 28px rgba(0,0,0,.25);
    overflow: hidden;
  }
  /* Front */
  .card-front {
    left: 440px; top: 40px;
    background: var(--brand-blue);
    color: var(--paper);
    display: flex; flex-direction: column; align-items: center; justify-content: center;
  }
  .brand { display: flex; align-items: center; gap: 14px; }
  .brand-dot {
    width: 44px; height: 44px; border-radius: 50%;
    background: var(--paper);
  }
  .brand-name {
    font-weight: 700; letter-spacing: .14em; text-transform: uppercase;
    color: var(--paper); line-height: 1.2;
  }
  .card-front .brand-name { font-size: 30px; }
  .card-front .site {
    margin-top: 46px; font-size: 17px; letter-spacing: .18em;
  }
  /* Back */
  .card-back { left: 60px; top: 460px; background: var(--paper); }
  .card-back .panel { position: absolute; inset: 0; }
  .card-back .brand {
    position: absolute; left: 36px; top: 120px; width: 300px;
  }
  .card-back .brand-dot { width: 34px; height: 34px; flex: none; }
  .card-back .brand-name { font-size: 19px; }
  .contact {
    position: absolute; left: 400px; top: 78px; color: var(--ink);
  }
  .contact .name { color: var(--brand-blue); font-size: 27px; font-weight: 400; }
  .contact .role { font-size: 17px; margin-bottom: 16px; }
  .contact .address { font-size: 18px; line-height: 1.3; margin-bottom: 14px; }
  .contact ul { list-style: none; font-size: 18px; line-height: 1.45; }
  .contact li { display: flex; align-items: center; gap: 12px; }
  .contact svg { width: 16px; height: 16px; fill: var(--brand-blue); flex: none; }
</style>
</head>
<body>
<div class="stage">

  <section class="card card-front">
    <div class="brand">
      <span class="brand-dot"></span>
      <span class="brand-name">Ridgeline Land &amp; Timber</span>
    </div>
    <p class="site">www.ridgelinetimber.com</p>
  </section>

  <section class="card card-back">
    <svg class="panel" viewBox="0 0 700 400" preserveAspectRatio="none">
      <polygon points="0,0 440,0 240,400 0,400" fill="var(--silver)"/>
      <polygon points="0,0 420,0 220,400 0,400" fill="var(--deep-blue)"/>
    </svg>
    <div class="brand">
      <span class="brand-dot"></span>
      <span class="brand-name">Ridgeline<br>Land &amp; Timber</span>
    </div>
    <div class="contact">
      <h1 class="name">Mark Ellison</h1>
      <p class="role">Manager</p>
      <p class="address">1450 Oak Bend Dr<br>Pinecrest TX 75000</p>
      <ul>
        <li><svg viewBox="0 0 16 16"><path d="M3 1h3l1 4-2 1c1 2 3 4 5 5l1-2 4 1v3c0 1-1 2-2 2C7 15 1 9 1 3c0-1 1-2 2-2z"/></svg>555 014 2200</li>
        <li><svg viewBox="0 0 16 16"><path d="M4 1h8v4H4zM1 6h14v6h-3v3H4v-3H1zM5 10v4h6v-4z"/></svg>555 014 2201</li>
        <li><svg viewBox="0 0 16 16"><path d="M1 3h14v10H1zM2 4l6 5 6-5z" fill-rule="evenodd"/></svg>info@ridgelinetimber.com</li>
        <li><svg viewBox="0 0 16 16"><circle cx="8" cy="8" r="7" fill="none" stroke="var(--brand-blue)" stroke-width="1.5"/><path d="M1 8h14M8 1c-3 3-3 11 0 14M8 1c3 3 3 11 0 14" fill="none" stroke="var(--brand-blue)" stroke-width="1.2"/></svg>www.ridgelinetimber.com</li>
      </ul>
    </div>
  </section>

</div>
</body>
</html>
```